Quiet Verses Across Winter Evenings

Need a BOOK COVER, SPINE, and BACK for above named book. This is the story of my late wife (a university professor) told through her own songs and poems. It is about the people she loved, especially her grand children, her extensive professional and life interests, her family, friends, and festivities, her illness, etc.
Updates

Need extra days to review

Target Market(s)

Family and friends

Font styles to use
Other font styles liked:
• Times New Roman

Requirements
Must have
• Regret I haven't given much thought to it...
Nice to have
• Regret I haven't given much thought to it..
Should not have

```html
<!DOCTYPE html>
<html lang="en">
<head>
<meta charset="utf-8">
<title>Quiet Verses Across Winter Evenings — Cover Spread</title>
<link rel="stylesheet" href="https://fonts.googleapis.com/css2?family=Cinzel:wght@400&family=EB+Garamond:wght@400&display=swap">
<style>
  :root {
    --canvas: #f3f3f1;
    --paper: #efefeb;
    --paper-light: #f7f7f4;
    --ink: #1c1c1a;
    --body-ink: #2a2a28;
    --field-olive: #b5a668;
    --field-gold: #c9b27a;
    --field-green: #8e9a62;
    --poppy: #e0643a;
    --ornament: #1d1d1b;
    --spine-line: rgba(0,0,0,0.06);
  }
  * { box-sizing: border-box; margin: 0; padding: 0; }
  html, body {
    width: 899px;
    height: 1200px;
    overflow: hidden;
    background: var(--canvas);
  }
  .spread {
    position: absolute;
    left: 20px;
    top: 302px;
    width: 859px;
    height: 596px;
    background: linear-gradient(180deg, var(--paper-light) 0%, var(--paper) 100%);
    box-shadow: 0 2px 10px rgba(0,0,0,0.12);
    overflow: hidden;
  }
  .field-photo {
    position: absolute;
    left: 0;
    right: 0;
    top: 280px;
    bottom: 0;
    background:
      linear-gradient(180deg,
        rgba(239,239,235,0) 0%,
        rgba(214,170,140,0.45) 22%,
        rgba(201,178,122,0.85) 48%,
        var(--field-olive) 75%,
        var(--field-green) 100%);
  }
  .panel { position: absolute; top: 0; bottom: 0; }
  .back { left: 0; width: 416px; }
  .spine {
    left: 416px;
    width: 31px;
    border-left: 1px solid var(--spine-line);
    border-right: 1px solid var(--spine-line);
  }
  .front { left: 447px; width: 412px; }

  .ornament {
    position: absolute;
    background: var(--ornament);
    border-radius: 14px;
    opacity: 0.85;
  }
  .back .ornament { left: 84px; top: 48px; width: 234px; height: 34px; }
  .front .ornament { left: 88px; top: 204px; width: 234px; height: 34px; }
  .spine .ornament { left: 4px; top: 524px; width: 22px; height: 28px; border-radius: 6px; }

  .blurb {
    position: absolute;
    left: 53px;
    top: 121px;
    width: 299px;
    font-family: "EB Garamond", "Times New Roman", serif;
    font-size: 10.4px;
    line-height: 13.2px;
    color: var(--body-ink);
    text-align: justify;
    hyphens: auto;
  }

  .spine-title {
    position: absolute;
    left: 50%;
    top: 40px;
    width: 280px;
    transform-origin: 0 0;
    transform: translateX(7px) rotate(90deg);
    font-family: "Cinzel", "Times New Roman", serif;
    font-size: 10px;
    letter-spacing: 0.02em;
    color: var(--ink);
    white-space: nowrap;
  }

  .author {
    position: absolute;
    left: 0;
    right: 0;
    top: 54px;
    text-align: center;
    font-family: "Cinzel", "Times New Roman", serif;
    font-size: 14px;
    letter-spacing: 0.36em;
    color: var(--ink);
    white-space: nowrap;
  }
  .title {
    position: absolute;
    left: 0;
    right: 0;
    top: 158px;
    text-align: center;
    font-family: "Cinzel", "Times New Roman", serif;
    font-weight: 400;
    font-size: 31px;
    letter-spacing: 0.01em;
    color: var(--ink);
  }
  .subtitle {
    position: absolute;
    left: 0;
    right: 0;
    top: 250px;
    text-align: center;
    font-family: "Cinzel", "Times New Roman", serif;
    font-weight: 400;
    font-size: 19px;
    color: var(--ink);
  }
</style>
</head>
<body>
  <main class="spread">
    <div class="field-photo" role="img" aria-label="Photograph of a wild meadow with red poppies and wheat stalks across the lower half of the cover"></div>

    <section class="panel back">
      <div class="ornament" role="img" aria-label="Decorative scroll flourish"></div>
      <p class="blurb">Lorem ipsum dolor sit amet, consectetur adipiscing elit. Maecenas ac mattis odio, quis ullamcorper massa. Mauris interdum massa felis, sed interdum sapien volutpat quis. Nullam sagittis orci tincidunt diam viverra, eget maximus est congue. Sed sed est scelerisque, accumsan urna nec, rhoncus dui. Sed efficitur sodales purus sit amet viverra. Nullam varius pretium luctus. Integer semper eget neque at ullamcorper. Nulla pulvinar, ante a interdum tempus, turpis lacus luctus massa, ac congue purus est ut quam. In tristique nunc felis, quis ullamcorper lorem rhoncus vitae. Integer ultrices in nisl sed rhoncus. Mauris magna elit, feugiat eget dapibus et, congue at tellus.</p>
    </section>

    <section class="panel spine">
      <p class="spine-title">Quiet Verses Across Winter Evenings</p>
      <div class="ornament" role="img" aria-label="Small decorative floral emblem"></div>
    </section>

    <section class="panel front">
      <p class="author">Meera Anand Kulkarni</p>
      <h1 class="title">QUIET VERSES</h1>
      <div class="ornament" role="img" aria-label="Decorative scroll flourish"></div>
      <p class="subtitle">ACROSS WINTER EVENINGS</p>
    </section>
  </main>
</body>
</html>
```